Business card and stationery concept for weight management and nutrition practice
trueLeaf Guidance
Dear Designers,
I have uploaded my logo files and am looking forward to everyone's designs.
I would like to see designs that do not feature my logo quite so prominently - that is, the logo does not have to be very large.
Also, instead of bold abstract curves and shapes I'd like to see accents that are more feminine.
Thanks everyone!
I like the bold concepts you have uploaded. I would also like to see more simple ideas, using the light blue and dark grey used in the logo rather than black.
I would also like to see a few concepts that are a bit more feminine. Not overtly so but subtle.
Thank you!
I am unable to upload my logo at this time -- I will do this on Saturday evening when I get back in town.

```html
<!DOCTYPE html>
<html lang="en">
<head>
<meta charset="utf-8">
<title>trueLeaf Guidance – Business Card</title>
<link rel="stylesheet" href="https://fonts.googleapis.com/css2?family=Raleway:wght@600&family=Open+Sans:wght@400;600&display=swap">
<style>
  :root {
    --page: #e9ebee;
    --card: #ffffff;
    --ink: #4a4a4c;
    --ink-soft: #6b6d70;
    --sky: #86a9c9;
    --band-light: #7a7b7e;
    --band-dark: #333436;
    --rule: #b9c3cc;
  }
  * { box-sizing: border-box; margin: 0; padding: 0; }
  html, body { width: 1200px; height: 980px; overflow: hidden; }
  body {
    background: var(--page);
    font-family: "Open Sans", Arial, sans-serif;
    color: var(--ink);
    display: flex;
    flex-direction: column;
    align-items: center;
    justify-content: center;
    gap: 28px;
  }
  .card {
    position: relative;
    width: 780px;
    height: 446px;
    background: var(--card);
    border-radius: 26px;
    overflow: hidden;
    box-shadow: 0 6px 18px rgba(0,0,0,0.12);
  }
  .brand { display: flex; align-items: center; gap: 14px; }
  .brand-dot {
    width: 22px; height: 22px;
    background: var(--sky);
    border-radius: 50%;
    flex: none;
  }
  .brand-name {
    font-family: "Raleway", Arial, sans-serif;
    font-weight: 600;
    color: var(--ink);
    letter-spacing: 0.5px;
    white-space: nowrap;
  }
  .card-front { display: flex; align-items: center; justify-content: center; }
  .card-front .brand-name { font-size: 40px; }

  .card-back .accent { position: absolute; left: 0; top: 0; }
  .card-back .brand { position: absolute; left: 72px; top: 168px; }
  .card-back .brand-name { font-size: 26px; }
  .card-back .brand-dot { width: 18px; height: 18px; }
  .divider {
    position: absolute;
    left: 372px; top: 110px;
    width: 1px; height: 186px;
    background: var(--rule);
  }
  .contact { position: absolute; left: 396px; top: 112px; }
  .person-name { font-size: 17px; font-weight: 600; color: var(--ink); }
  .person-role { font-size: 14px; color: var(--ink-soft); margin-top: 3px; }
  .contact-list { list-style: none; margin-top: 20px; }
  .contact-list li {
    display: flex; align-items: flex-start; gap: 9px;
    font-size: 13.5px; line-height: 1.45; color: var(--ink-soft);
    margin-bottom: 6px;
  }
  .contact-list svg { flex: none; margin-top: 2px; }
</style>
</head>
<body>

<section class="card card-front" aria-label="Business card front">
  <div class="brand">
    <span class="brand-dot"></span>
    <span class="brand-name">trueLeaf Guidance</span>
  </div>
</section>

<section class="card card-back" aria-label="Business card back">
  <svg class="accent" width="780" height="446" viewBox="0 0 780 446" aria-hidden="true">
    <defs>
      <linearGradient id="cornerShade" x1="0" y1="0" x2="1" y2="0">
        <stop offset="0" stop-color="var(--band-dark)"/>
        <stop offset="0.7" stop-color="var(--band-light)"/>
        <stop offset="1" stop-color="var(--band-dark)"/>
      </linearGradient>
    </defs>
    <path d="M0 362 Q 240 392, 520 446 L 0 446 Z" fill="url(#cornerShade)"/>
    <path d="M0 346 Q 250 376, 560 446" fill="none" stroke="var(--sky)" stroke-width="2"/>
  </svg>

  <div class="brand">
    <span class="brand-dot"></span>
    <span class="brand-name">trueLeaf Guidance</span>
  </div>

  <div class="divider"></div>

  <div class="contact">
    <p class="person-name">Nora J. Halvers, MS, RD, LDN</p>
    <p class="person-role">Registered Dietitian</p>
    <ul class="contact-list">
      <li>
        <svg width="13" height="15" viewBox="0 0 13 15"><path d="M6.5 0.5a5 5 0 0 1 5 5c0 3.6-5 9-5 9s-5-5.4-5-9a5 5 0 0 1 5-5z" fill="var(--ink-soft)"/><circle cx="6.5" cy="5.5" r="1.8" fill="#fff"/></svg>
        <span>418 North Alder Street<br>Maplewood, Ohio 45340</span>
      </li>
      <li>
        <svg width="14" height="12" viewBox="0 0 14 12"><rect x="0.5" y="1" width="13" height="10" rx="1.5" fill="var(--ink-soft)"/><path d="M1 2l6 4.5L13 2" fill="none" stroke="#fff" stroke-width="1.2"/></svg>
        <span>trueleafguidance@mail.com</span>
      </li>
      <li>
        <svg width="14" height="14" viewBox="0 0 14 14"><circle cx="7" cy="7" r="6" fill="none" stroke="var(--ink-soft)" stroke-width="1.4"/><ellipse cx="7" cy="7" rx="2.6" ry="6" fill="none" stroke="var(--ink-soft)" stroke-width="1.1"/><path d="M1 7h12" stroke="var(--ink-soft)" stroke-width="1.1"/></svg>
        <span>www.trueleafguidance.com</span>
      </li>
    </ul>
  </div>
</section>

</body>
</html>
```